Cloudmarra label design 2.5 x 3.5 in size can go either way

need a label design created for a eliquid line called cloudmarra the line was called lanternfall but there are a few other companies out there going by the same name so we are trying to rebrand there is a company called tollgate brewing company and i really like the looks of all there boxes and labels so I want the label to resemble the style of there labels but be unique to us we have 7 flavors so each label can have the same basic layout but a different color for each name and flavor i will attach pictures of the old label and ideas for the new label we want to stick to a lanternfall era/ mobster kinda look the flavors are:
gusto
tinsel
moonharvest
cold snap
march 3rd
pinwheel
fig
I also attached some of our other lines pictures for reference as to how its gonna be used

Target Market(s)

Vapers

Colors

Requirements
Must have
• if you look at the lanternfall label I posted in the pictures it will show the things that have to be included
• Nicotine Content
• Made in USA
• ISO 7 certified
• cloudmarra name on top
• flavor name on bottom
• nicotine warning or space on side of label that I can add
Nice to have
• bold colors for the name and flavor rest in greyscale

```html
<!DOCTYPE html>
<html lang="en">
<head>
<meta charset="utf-8">
<title>Cloudmarra Label Colourways</title>
<link rel="stylesheet" href="https://fonts.googleapis.com/css2?family=Josefin+Sans:wght@300;400&display=swap">
<style>
  :root {
    --page: #f2f2f2;
    --ink-dark: #1a1a1a;
    --mono-label: #111111;
    --mono-frame: #7a7a7a;
    --mono-text: #c4c4c4;
    --mono-smoke: #ededed;
    --mono-figure: #4a4a4a;
    --mono-deep: #161616;
    --gold-label: #16130a;
    --gold-frame: #8a7422;
    --gold-text: #c9a522;
    --gold-smoke: #f2c419;
    --gold-figure: #5e4e0e;
    --gold-deep: #1a1606;
  }
  * { box-sizing: border-box; margin: 0; padding: 0; }
  html, body { width: 1200px; height: 1200px; overflow: hidden; }
  body {
    background: var(--page);
    font-family: "Josefin Sans", sans-serif;
    display: flex;
    align-items: center;
    justify-content: center;
    gap: 70px;
  }
  .label {
    position: relative;
    width: 470px;
    height: 650px;
    overflow: hidden;
    background: var(--label-bg);
    --label-bg: var(--mono-label);
    --frame: var(--mono-frame);
    --accent: var(--mono-text);
    --smoke: var(--mono-smoke);
    --figure: var(--mono-figure);
    --deep: var(--mono-deep);
    --ribbon: #f4f4f4;
  }
  .label--gold {
    --label-bg: var(--gold-label);
    --frame: var(--gold-frame);
    --accent: var(--gold-text);
    --smoke: var(--gold-smoke);
    --figure: var(--gold-figure);
    --deep: var(--gold-deep);
    --ribbon: var(--gold-smoke);
  }
  .label__photo {
    position: absolute;
    left: 34px;
    top: 34px;
    right: 0;
    bottom: 48px;
    background:
      linear-gradient(200deg, transparent 55%, var(--smoke) 100%),
      linear-gradient(90deg, var(--figure) 0%, var(--deep) 62%, var(--deep) 100%);
  }
  .label__frame {
    position: absolute;
    left: 22px;
    top: 22px;
    width: 426px;
    height: 580px;
    pointer-events: none;
  }
  .label__frame path, .label__frame rect { stroke: var(--frame); fill: none; }
  .label__title {
    position: absolute;
    top: 52px;
    right: 50px;
    color: var(--accent);
    font-weight: 300;
  }
  .label__name { font-size: 32px; letter-spacing: 1px; line-height: 1; }
  .label__nicotine { font-size: 17px; margin-top: 6px; }
  .label__brand {
    position: absolute;
    top: 300px;
    right: 50px;
    width: 200px;
    text-align: center;
    color: var(--accent);
    font-weight: 400;
    font-size: 30px;
    line-height: 1.05;
    letter-spacing: 1px;
    text-transform: uppercase;
  }
  .label__brand small {
    display: block;
    font-size: 14px;
    letter-spacing: 4px;
    margin-top: 6px;
  }
  .label__flavour {
    position: absolute;
    left: 44px;
    bottom: 82px;
    background: var(--ribbon);
    color: var(--ink-dark);
    font-size: 19px;
    font-weight: 400;
    padding: 8px 34px 6px 28px;
    clip-path: polygon(0 0, 100% 0, 92% 100%, 0 100%);
  }
  .label__origin {
    position: absolute;
    left: 78px;
    bottom: 14px;
    color: var(--accent);
    font-size: 20px;
    font-weight: 300;
  }
</style>
</head>
<body>
  <section class="label label--mono">
    <div class="label__photo" role="img" aria-label="Greyscale photo of a man in a fedora exhaling a large cloud of vapour"></div>
    <svg class="label__frame" viewBox="0 0 426 580" aria-hidden="true">
      <path d="M14 1 H412 M14 1 A13 13 0 0 1 1 14 V566 A13 13 0 0 1 14 579 H412 M412 1 A13 13 0 0 0 425 14 V566" stroke-width="2"/>
      <rect x="12" y="12" width="402" height="556" stroke-width="1"/>
    </svg>
    <div class="label__title">
      <p class="label__name">CLOUDMARRA</p>
      <p class="label__nicotine">NICOTINE CONTENT</p>
    </div>
    <p class="label__brand">Tollgate<small>brewing company</small></p>
    <p class="label__flavour">COCONUT FLAVOUR</p>
    <p class="label__origin">MADE IN USA</p>
  </section>

  <section class="label label--gold">
    <div class="label__photo" role="img" aria-label="Gold-toned photo of a man in a fedora exhaling a large cloud of vapour"></div>
    <svg class="label__frame" viewBox="0 0 426 580" aria-hidden="true">
      <path d="M14 1 H412 M14 1 A13 13 0 0 1 1 14 V566 A13 13 0 0 1 14 579 H412 M412 1 A13 13 0 0 0 425 14 V566" stroke-width="2"/>
      <rect x="12" y="12" width="402" height="556" stroke-width="1"/>
    </svg>
    <div class="label__title">
      <p class="label__name">CLOUDMARRA</p>
      <p class="label__nicotine">NICOTINE CONTENT</p>
    </div>
    <p class="label__brand">Tollgate<small>brewing company</small></p>
    <p class="label__flavour">COCONUT FLAVOUR</p>
    <p class="label__origin">MADE IN USA</p>
  </section>
</body>
</html>
```